Wine Company Flyer Design

Hello,

I need a flyer design that will fit an 11 inch width by 17 inch height. Design has to be submitted in PDF X-1a format.

We want our logo on the flyer with the slogan underneath it saying "Better Wines Lower Prices"

We want a nice design and then we will get to some of the text that will be on the flyer.

Please make the flyer in two colors ONLY. Use the colors of our logo for the rest of the design.

Requirements
Must have
• PDF x-1a format
• Logo on flyer with slogan "Better Wines Lower Prices" underneath
• Two colors - Orange, Red (Same as logo colors)
• Fits in an 11"x17" format for printing
• This will be for the wine industry so include elements of wine in the flyer and make it look nice. Leave some space in the middle of the design for text to be put in.

```html
<!DOCTYPE html>
<html lang="en">
<head>
<meta charset="utf-8">
<title>Corkhouse Flyer</title>
<link href="https://fonts.googleapis.com/css2?family=Bebas+Neue&family=Raleway:wght@300;700&family=Roboto+Condensed:wght@400&display=swap" rel="stylesheet">
<style>
  :root{
    --red:#e0182d;
    --orange:#f2a457;
    --brown:#b95e2b;
    --grey:#bcc6c5;
    --white:#ffffff;
    --ink:#1d1d1d;
    --icon:#6d6f70;
  }
  *{margin:0;padding:0;box-sizing:border-box}
  html,body{width:800px;height:1200px;overflow:hidden;background:var(--white)}
  .flyer{position:relative;width:800px;height:1200px;overflow:hidden;background:var(--white);font-family:'Roboto Condensed',sans-serif}
  .shapes,.photo{position:absolute;left:0;top:0}
  .brand{position:absolute;left:60px;top:126px;display:flex;align-items:center;gap:8px}
  .brand-dot{width:14px;height:14px;border-radius:50%;background:var(--orange)}
  .brand-name{font-family:'Bebas Neue',sans-serif;font-size:34px;line-height:1;color:var(--red);letter-spacing:0.5px}
  .headline{position:absolute;font-family:'Bebas Neue',sans-serif;text-transform:uppercase;transform-origin:left top;font-weight:400}
  .headline span{display:block}
  .slogan{left:534px;top:104px;font-size:68px;line-height:80px;transform:scaleX(0.87)}
  .slogan .warm{color:var(--orange)}
  .slogan .hot{color:var(--red)}
  .party{left:108px;top:270px;font-size:46px;line-height:54.5px;color:var(--white);transform:scaleX(0.9)}
  .party .hot{color:var(--red)}
  .section{position:absolute;left:59px;width:340px;color:var(--white)}
  .section h2{font-family:'Raleway',sans-serif;font-weight:700;font-size:20px;line-height:24px}
  .section .rule{width:77px;height:2px;background:var(--white);margin:9px 0 9px}
  .about{top:568px}
  .about p{font-size:14.4px;line-height:17.6px;white-space:nowrap}
  .why{top:776px}
  .why ul{list-style:none}
  .why li{display:flex;gap:10px;font-size:14.4px;line-height:17.6px;margin-bottom:11.2px;white-space:nowrap}
  .why svg{flex:none;margin-top:7px}
  .feature{position:absolute;left:494px;width:290px;color:var(--ink)}
  .feature .icon{display:block;width:48px;height:50px;margin-bottom:10px}
  .feature .kicker{font-family:'Raleway',sans-serif;font-weight:300;font-size:21px;line-height:24px}
  .feature h3{font-family:'Raleway',sans-serif;font-weight:700;font-size:21px;line-height:28px}
  .feature p{font-size:14.4px;line-height:17.6px;text-transform:uppercase;margin-top:11px;white-space:nowrap}
  .contact{position:absolute;left:62px;top:1133px;border-left:2px solid var(--white);padding-left:12px;color:var(--white);font-size:13px;line-height:16px;font-style:normal}
</style>
</head>
<body>
<div class="flyer">
  <svg class="shapes" width="800" height="1200" viewBox="0 0 800 1200" aria-hidden="true">
    <path d="M36,262 C150,252 270,232 370,192 L370,420 L36,420 Z" fill="var(--red)"/>
    <path d="M24,272 C150,258 290,254 388,222 L388,1104 L24,1104 Z" fill="var(--grey)"/>
    <path d="M0,546 C90,508 190,516 270,524 C340,530 380,500 408,478 L408,940 C370,990 300,1000 210,1010 C120,1020 40,1060 0,1090 Z" fill="var(--brown)"/>
    <path d="M24,1102 C130,1070 260,1062 388,1022 L388,1200 L24,1200 Z" fill="var(--red)"/>
  </svg>

  <svg class="photo" width="800" height="520" viewBox="0 0 800 520" role="img" aria-label="Photo of dark wine bottles lying side by side on a wooden table">
    <defs>
      <linearGradient id="tableTone" x1="0" y1="0" x2="1" y2="1">
        <stop offset="0" stop-color="#4a3a32"/>
        <stop offset="0.4" stop-color="#b8693a"/>
        <stop offset="0.7" stop-color="#7a4a30"/>
        <stop offset="1" stop-color="#2c2a29"/>
      </linearGradient>
    </defs>
    <path d="M408,0 H800 V516 C760,500 720,468 660,458 C600,450 560,470 500,478 C460,484 430,484 408,480 Z" fill="url(#tableTone)"/>
  </svg>

  <div class="brand">
    <span class="brand-dot"></span>
    <span class="brand-name">CORKHOUSE</span>
  </div>

  <h1 class="headline slogan">
    <span class="warm">Better</span>
    <span class="hot">Wines</span>
    <span class="warm">Lower</span>
    <span class="hot">Prices</span>
  </h1>

  <div class="headline party">
    <span class="hot">Best</span>
    <span>Party</span>
    <span>With Red</span>
    <span class="hot">Wines</span>
  </div>

  <section class="section about">
    <h2>ABOUT US</h2>
    <div class="rule"></div>
    <p>Lorem ipsum dolor sit amet, consectk adipisicing<br>elit, sed do eiusmod tempor incididunt ut laborele<br>et dolore magna aliqua. Ut enim minim veniamll,<br>quis nostrud exercitation ullamco laboris nisi utp<br>aliquip ex ea commodo consequat. Duis autcirure<br>dolor in reprehenderit in voluptate velit essecillum<br>dolore eu fugiat nulla pariatur. Excepteu occaecat</p>
  </section>

  <section class="section why">
    <h2>WHY CHOOSE US?</h2>
    <div class="rule"></div>
    <ul>
      <li><svg width="19" height="19" viewBox="0 0 20 20"><circle cx="10" cy="10" r="8.5" fill="none" stroke="#fff" stroke-width="2"/><path d="M6,10.3 L9,13 L14,7.5" fill="none" stroke="#fff" stroke-width="2"/></svg><span>Lorem ipsum dolor sit amet, consectetur adipisici<br>elit, sed do eiusmod.</span></li>
      <li><svg width="19" height="19" viewBox="0 0 20 20"><circle cx="10" cy="10" r="8.5" fill="none" stroke="#fff" stroke-width="2"/><path d="M6,10.3 L9,13 L14,7.5" fill="none" stroke="#fff" stroke-width="2"/></svg><span>Lorem ipsum dolor sit amet, consectetur adipisici<br>elit, sed do eiusmod.</span></li>
      <li><svg width="19" height="19" viewBox="0 0 20 20"><circle cx="10" cy="10" r="8.5" fill="none" stroke="#fff" stroke-width="2"/><path d="M6,10.3 L9,13 L14,7.5" fill="none" stroke="#fff" stroke-width="2"/></svg><span>Lorem ipsum dolor sit amet, consectetur adipisici<br>elit, sed do eiusmod.</span></li>
    </ul>
  </section>

  <article class="feature" style="top:550px">
    <svg class="icon" viewBox="0 0 48 50" aria-hidden="true"><path d="M2,24 L46,4 L30,46 L22,30 Z M22,30 L46,4 M22,30 L22,42 L28,35" fill="none" stroke="var(--icon)" stroke-width="2.5" stroke-linejoin="round"/></svg>
    <div class="kicker">Creative</div>
    <h3>Design</h3>
    <p>Lorem ipsum dolor sit amet, klmn<br>consectetur adipisicing elit, sed d<br>o eiusmod tempor incididunt ut op</p>
  </article>

  <article class="feature" style="top:768px">
    <svg class="icon" viewBox="0 0 48 50" aria-hidden="true"><circle cx="28" cy="18" r="15" fill="none" stroke="var(--icon)" stroke-width="2.5"/><path d="M17,29 L5,44 C3,47 6,49 8,47 L20,32" fill="none" stroke="var(--icon)" stroke-width="2.5"/><path d="M21,12 C23,8 27,7 30,7" fill="none" stroke="var(--icon)" stroke-width="2"/></svg>
    <div class="kicker">Creative</div>
    <h3>Branding</h3>
    <p>Lorem ipsum dolor sit amet, klmn<br>consectetur adipisicing elit, sed d<br>o eiusmod tempor incididunt ut op</p>
  </article>

  <article class="feature" style="top:982px">
    <svg class="icon" viewBox="0 0 48 50" aria-hidden="true"><path d="M4,48 L14,24 L36,2 L46,12 L26,34 Z M4,48 L18,36 M22,16 L32,26 M27,11 L37,21" fill="none" stroke="var(--icon)" stroke-width="2.5" stroke-linejoin="round"/></svg>
    <div class="kicker">Creative</div>
    <h3>Marketing</h3>
    <p>Lorem ipsum dolor sit amet, klmn<br>consectetur adipisicing elit, sed d<br>o eiusmod tempor incididunt ut op</p>
  </article>

  <address class="contact">
    42 Vine Row, Cellar Lane 7, Country.<br>
    Phone: +00-555-210-3344, +00-555-210-3345<br>
    Email: hello@corkhouse.com
  </address>
</div>
</body>
</html>
```